Word Cloud Graphic Wallpaper design

The following sentences need to be put together in an ai file of the size : 70" wide and 108" high . This will be used as a wall paper. Inspirational image is attached. (We have also attached a rough idea showing you the wall it would go one- DO NOT REPLICATE THE LAYOUT OF THE SENTENCES-This only shows you how we will be using your file)

Sentences are:

Dentistry is not Expensive Neglect is!
Smiles are free but they are worth alot.
Don't Forget to Floss!
Put on your best SMILE everyday!
Be the reason someone smiles today.
Let your SMILE CHANGE THE WORLD, don't let the world change your smile.
Make your smile your signature accessory!

These should be in different fonts (clean modern fonts only please- no cursive or busy fonts - Helvetica Neue, Arial and fonts such as those are preferred) and sizes and should be easily legible (minimum font height 4"). Repetitions are ok if needed to fill space.

Font styles to use
Sans Serif

Requirements
Must have
• hese should be in different fonts (clean modern fonts only please- no cursive or busy fonts - Helvetica Neue, Arial and fonts such as those) and sizes and should be easily legible (minimum font height 4"). Repetitions are ok if needed to fill space.
Should not have
• Cursive, busy, fonts.

```html
<!DOCTYPE html>
<html lang="en">
<head>
<meta charset="utf-8">
<title>Smile Word Wall</title>
<link rel="stylesheet" href="https://fonts.googleapis.com/css2?family=Arimo:wght@400&family=Montserrat:wght@800&family=Roboto+Condensed:wght@300&family=Roboto:wght@100;300&display=swap">
<style>
  :root{
    --green:#55e61c;
    --lime:#88ee11;
    --teal:#33dd99;
    --sea:#33cc88;
    --orange:#ff6a1a;
    --amber:#ffc90e;
    --cyan:#11eaff;
    --pink:#ff0a6a;
    --pink-soft:#ffd3e3;
    --coral:#ff7733;
    --gold:#eecc00;
    --paper:#ffffff;
  }
  html,body{margin:0;padding:0;overflow:hidden;background:var(--paper);}
  .wallpaper{display:block;width:778px;height:1200px;}
  .bold{font-family:"Montserrat",sans-serif;font-weight:800;}
  .regular{font-family:"Arimo",sans-serif;font-weight:400;}
  .narrow{font-family:"Roboto Condensed",sans-serif;font-weight:300;}
  .thin{font-family:"Roboto",sans-serif;font-weight:100;}
  .light{font-family:"Roboto",sans-serif;font-weight:300;}
  .c-green{fill:var(--green);}
  .c-lime{fill:var(--lime);}
  .c-teal{fill:var(--teal);}
  .c-sea{fill:var(--sea);}
  .c-orange{fill:var(--orange);}
  .c-amber{fill:var(--amber);}
  .c-cyan{fill:var(--cyan);}
  .c-pink{fill:var(--pink);}
  .c-coral{fill:var(--coral);}
</style>
</head>
<body>
<svg class="wallpaper" viewBox="0 0 972 1500" xmlns="http://www.w3.org/2000/svg">
  <defs>
    <linearGradient id="emoticon-tone" x1="0" y1="0" x2="0" y2="1">
      <stop offset="0" stop-color="var(--pink-soft)"/>
      <stop offset="1" stop-color="#ffb3cf"/>
    </linearGradient>
  </defs>

  <g class="band band-top">
    <rect x="0" y="0" width="139" height="18" fill="#33bb77"/>
    <rect x="139" y="0" width="139" height="18" fill="var(--teal)"/>
    <rect x="278" y="0" width="139" height="18" fill="var(--green)"/>
    <rect x="417" y="0" width="139" height="18" fill="#99ee11"/>
    <rect x="556" y="0" width="139" height="18" fill="var(--gold)"/>
    <rect x="695" y="0" width="139" height="18" fill="var(--coral)"/>
    <rect x="834" y="0" width="138" height="18" fill="var(--pink)"/>
  </g>

  <text class="narrow c-green" x="42" y="100" font-size="84" textLength="898" lengthAdjust="spacingAndGlyphs">Dentistry is not Expensive Neglect is!</text>

  <text class="bold c-teal" x="42" y="228" font-size="124" textLength="448" lengthAdjust="spacingAndGlyphs">SMILES</text>
  <text class="regular c-teal" x="517" y="228" font-size="118" textLength="423" lengthAdjust="spacingAndGlyphs">are Free</text>

  <text class="regular c-teal" x="45" y="325" font-size="98" textLength="895" lengthAdjust="spacingAndGlyphs">but they are worth a lot.</text>

  <text class="regular c-green" x="45" y="425" font-size="98" textLength="895" lengthAdjust="spacingAndGlyphs">Don't Forget to Floss!</text>

  <text class="narrow c-lime" x="45" y="535" font-size="102" textLength="423" lengthAdjust="spacingAndGlyphs">Put on Your Best</text>
  <text class="bold c-lime" x="490" y="540" font-size="128" textLength="448" lengthAdjust="spacingAndGlyphs">SMILES</text>

  <text class="regular c-orange" x="40" y="630" font-size="88" textLength="427" lengthAdjust="spacingAndGlyphs">Be the Reason</text>
  <text class="thin c-green" x="503" y="630" font-size="86" textLength="437" lengthAdjust="spacingAndGlyphs">EVERYDAY!</text>

  <text class="regular c-orange" x="40" y="722" font-size="142" textLength="430" lengthAdjust="spacingAndGlyphs">someone</text>
  <text class="bold c-orange" x="38" y="822" font-size="110" textLength="432" lengthAdjust="spacingAndGlyphs">SMILES</text>
  <text class="thin c-orange" x="40" y="907" font-size="90" textLength="428" lengthAdjust="spacingAndGlyphs">TODAY.</text>

  <g class="vertical-stack">
    <text class="light c-amber" transform="translate(562 905) rotate(-90)" font-size="96" textLength="255" lengthAdjust="spacingAndGlyphs">Put on</text>
    <text class="light c-amber" transform="translate(662 905) rotate(-90)" font-size="104" textLength="255" lengthAdjust="spacingAndGlyphs">Your</text>
    <text class="regular c-amber" transform="translate(742 905) rotate(-90)" font-size="108" textLength="255" lengthAdjust="spacingAndGlyphs">Best</text>
    <text class="bold c-amber" transform="translate(866 905) rotate(-90)" font-size="146" textLength="257" lengthAdjust="spacingAndGlyphs">SMILES</text>
    <text class="thin" transform="translate(938 1120) rotate(-90)" font-size="68" textLength="470" lengthAdjust="spacingAndGlyphs"><tspan class="c-amber">EVER</tspan><tspan class="c-green">YDAY!</tspan></text>
  </g>

  <text class="regular c-cyan" x="45" y="1005" font-size="98" textLength="410" lengthAdjust="spacingAndGlyphs">Let your</text>
  <text class="bold c-cyan" x="485" y="1020" font-size="128" textLength="381" lengthAdjust="spacingAndGlyphs">SMILE</text>

  <text class="narrow c-cyan" x="45" y="1125" font-size="112" textLength="817" lengthAdjust="spacingAndGlyphs">CHANGE THE WORLD,</text>

  <text class="narrow c-cyan" x="45" y="1212" font-size="84" textLength="587" lengthAdjust="spacingAndGlyphs">don't let the world change your</text>
  <text class="bold c-cyan" x="640" y="1220" font-size="100" textLength="300" lengthAdjust="spacingAndGlyphs">SMILE.</text>

  <text class="narrow c-green" x="45" y="1308" font-size="82" textLength="200" lengthAdjust="spacingAndGlyphs">Make your</text>
  <text class="bold c-green" x="260" y="1315" font-size="86" textLength="206" lengthAdjust="spacingAndGlyphs">SMILE</text>
  <text class="narrow c-green" x="480" y="1310" font-size="82" textLength="463" lengthAdjust="spacingAndGlyphs">your signature accessory!</text>

  <text class="bold" x="45" y="1455" font-size="150" textLength="445" lengthAdjust="spacingAndGlyphs"><tspan class="c-sea">S</tspan><tspan class="c-lime">M</tspan><tspan class="c-coral">I</tspan><tspan class="c-cyan">L</tspan><tspan class="c-pink">E</tspan></text>

  <rect class="emoticon-area" x="502" y="1372" width="130" height="76" rx="10" fill="url(#emoticon-tone)" role="img" aria-label="Pink smiling emoticon"/>

  <text class="regular c-sea" x="645" y="1448" font-size="106" textLength="295" lengthAdjust="spacingAndGlyphs">Please!</text>

  <g class="band band-bottom">
    <rect x="0" y="1482" width="139" height="18" fill="var(--pink)"/>
    <rect x="139" y="1482" width="139" height="18" fill="var(--coral)"/>
    <rect x="278" y="1482" width="139" height="18" fill="var(--gold)"/>
    <rect x="417" y="1482" width="139" height="18" fill="#99ee11"/>
    <rect x="556" y="1482" width="139" height="18" fill="var(--green)"/>
    <rect x="695" y="1482" width="139" height="18" fill="var(--teal)"/>
    <rect x="834" y="1482" width="138" height="18" fill="#33bb77"/>
  </g>
</svg>
</body>
</html>
```